Dental Lab flyer

I would like eye catching dental lab flyer. Promoting Q.vex , Birelo Zirconia, and 7K Duvo Prisma Zirconia.
Price Q.vex $85
Birelo $44
7K $56

```html
<!DOCTYPE html>
<html lang="en">
<head>
<meta charset="utf-8">
<title>Lab Promotion Flyer</title>
<link href="https://fonts.googleapis.com/css2?family=Poppins:wght@400;700&display=swap" rel="stylesheet">
<style>
  :root {
    --backdrop: #c4c4c4;
    --paper: #ffffff;
    --ink: #231f20;
    --on-dark: #ffffff;
  }
  * { margin: 0; padding: 0; box-sizing: border-box; }
  html, body {
    width: 1065px;
    height: 1200px;
    overflow: hidden;
    background: var(--backdrop);
    font-family: "Poppins", Arial, sans-serif;
    color: var(--ink);
  }
  .flyer {
    position: absolute;
    left: 129px;
    top: 60.5px;
    width: 831px;
    height: 1075.6px;
    overflow: hidden;
    background: var(--paper);
    box-shadow: 2px 3px 6px rgba(0,0,0,0.25);
  }
  .flyer-inner {
    position: absolute;
    left: 0; top: 0;
    width: 1416px;
    height: 1832px;
    transform: scale(0.5871);
    transform-origin: 0 0;
  }
  .shapes { position: absolute; left: 0; top: 0; width: 1416px; height: 1832px; }

  .brand-box {
    position: absolute;
    left: 1027px; top: 78px;
    width: 389px; height: 262px;
    background: var(--ink);
    color: var(--on-dark);
    display: flex;
    flex-direction: column;
    align-items: center;
    justify-content: center;
    gap: 22px;
    padding-top: 10px;
  }
  .brand-mark {
    width: 54px; height: 54px;
    border: 3px solid var(--on-dark);
    border-radius: 50%;
  }
  .brand-name {
    font-size: 22px;
    font-weight: 400;
    letter-spacing: 2.2px;
    text-transform: uppercase;
    white-space: nowrap;
  }

  .headline {
    position: absolute;
    left: 89px; top: 466px;
    color: var(--on-dark);
    font-weight: 700;
    font-size: 70px;
    line-height: 82px;
    text-transform: uppercase;
  }

  .contact {
    position: absolute;
    left: 955px; top: 628px;
    font-weight: 700;
    white-space: nowrap;
  }
  .contact-row { display: flex; align-items: center; gap: 20px; }
  .contact-row svg { width: 36px; height: 36px; flex: none; }
  .contact-phone { font-size: 55px; line-height: 62px; }
  .contact-web { font-size: 50px; line-height: 56px; }

  .offer-panel {
    position: absolute;
    left: 597px; top: 1068px;
    width: 819px; height: 333px;
    background: var(--ink);
    border-radius: 32px 0 0 32px;
  }

  .product-photo {
    position: absolute;
    width: 266px; height: 266px;
    border-radius: 50%;
  }
  .photo-crown { left: 72px; top: 772px; background: radial-gradient(circle at 48% 52%, #e8e3da 0 28%, #8c8f88 42%, #0a0a0a 62%); }
  .photo-bond { left: 634px; top: 1100px; background: radial-gradient(circle at 42% 55%, #f2f2f2 0 30%, #3a3a3a 52%, #fbfbfb 58%); }
  .photo-bridge { left: 238px; top: 1461px; background: linear-gradient(160deg, #0a0a0a 0 45%, #d9d2c4 70%, #f3efe8 100%); }

  .offer { position: absolute; }
  .offer-name { font-size: 57px; font-weight: 400; line-height: 66px; }
  .offer-price { font-size: 60px; font-weight: 700; line-height: 66px; margin-top: -2px; }
  .offer-text { font-size: 26.5px; font-weight: 400; line-height: 30.5px; margin-top: 10px; }
  .offer-on-dark { color: var(--on-dark); }

  .offer-qvex { left: 376px; top: 790px; width: 560px; }
  .offer-7k { left: 937px; top: 1100px; width: 460px; }
  .offer-birelo { left: 543px; top: 1470px; width: 560px; }

  .footer-band {
    position: absolute;
    left: 0; top: 1787px;
    width: 1416px; height: 45px;
    background: var(--ink);
  }
</style>
</head>
<body>
  <main class="flyer">
    <div class="flyer-inner">
      <svg class="shapes" viewBox="0 0 1416 1832">
        <defs>
          <linearGradient id="hero-tones" x1="0" y1="0" x2="1" y2="1">
            <stop offset="0" stop-color="#8a5a4a"/>
            <stop offset="0.35" stop-color="#b88a72"/>
            <stop offset="0.6" stop-color="#c9c0b0"/>
            <stop offset="1" stop-color="#e4e1dc"/>
          </linearGradient>
        </defs>
        <path role="img" aria-label="Photo of a dentist with gloved hands examining a young patient's teeth"
              d="M0 0 H1005 L1245 330 C1268 372 1258 420 1238 458 C1210 508 1172 530 1130 540 L0 742 Z"
              fill="url(#hero-tones)"/>
      </svg>

      <div class="brand-box">
        <span class="brand-mark"></span>
        <span class="brand-name">Crownwell Dental</span>
      </div>

      <h1 class="headline">Lab<br>Promotion</h1>

      <div class="contact">
        <div class="contact-row contact-phone">
          <svg viewBox="0 0 24 24" fill="none" stroke="#231f20" stroke-width="1.4" stroke-linejoin="round">
            <path d="M6.5 3.5l3 3.5-1.8 2.2c1.2 2.6 3.2 4.6 5.8 5.8l2.2-1.8 3.5 3-2 3c-6.5-.5-12.7-6.7-13.2-13.2z"/>
          </svg>
          <span>+000 000 00</span>
        </div>
        <div class="contact-row contact-web">
          <svg viewBox="0 0 24 24" fill="none" stroke="#231f20" stroke-width="1.6">
            <rect x="3" y="6" width="18" height="13"/>
            <path d="M3 6l9 7 9-7M3 19l7-6M21 19l-7-6"/>
          </svg>
          <span>www.cwl.com</span>
        </div>
      </div>

      <div class="product-photo photo-crown" role="img" aria-label="Photo of a ceramic crown on a black background"></div>
      <div class="offer offer-qvex">
        <h2 class="offer-name">Q.vex</h2>
        <p class="offer-price">$85</p>
        <p class="offer-text">Lorem ipsum dolor sit amet, consectetuer adipiscing elit, sed diam nonummy nibh euismod tinc</p>
      </div>

      <div class="offer-panel"></div>
      <div class="product-photo photo-bond" role="img" aria-label="Photo of a bonding agent bottle and syringe"></div>
      <div class="offer offer-7k offer-on-dark">
        <h2 class="offer-name">7K</h2>
        <p class="offer-price">$56</p>
        <p class="offer-text">Lorem ipsum dolor sit amet, consectetuer adipiscing elit, sed diam nonummy nibh euismod tinc</p>
      </div>

      <div class="product-photo photo-bridge" role="img" aria-label="Photo of zirconia front teeth on a black background"></div>
      <div class="offer offer-birelo">
        <h2 class="offer-name">Birelo</h2>
        <p class="offer-price">$44</p>
        <p class="offer-text">Lorem ipsum dolor sit amet, consectetuer adipiscing elit, sed diam nonummy nibh euismod tinc</p>
      </div>

      <div class="footer-band"></div>
    </div>
  </main>
</body>
</html>
```